Personal Injury Lawyer Billboard

I would like a design created featuring the image of the lawyer centered in the middle of the design.
To the left of the lawyer's image it should read "INJURED?"
To the right of the lawyer's image, it should read "CALL BRUNO!"
Under Call Bruno, include the phone number 318-555-0187.
At the bottom of the design include the lawyers information "Bruno Pemberly Accident & Injury Lawyers"
PLEASE REMOVED THE BACKGROUND IMAGERY OF THE PHOTO SUBMITTED. Also, the colors for this design should match the colors shown in the logo (navy, white and relective soft gold). Please use those color combinations in ways that best stand out.

```html
<!DOCTYPE html>
<html lang="en">
<head>
<meta charset="utf-8">
<title>Bruno Pemberly Billboard</title>
<link rel="stylesheet" href="https://fonts.googleapis.com/css2?family=Bebas+Neue&display=swap">
<style>
  :root {
    --page: #eef0f3;
    --navy: #16306e;
    --navy-deep: #0f1f4d;
    --blue: #1f4da3;
    --gold: #f1bb1b;
    --gold-soft: #e9b43a;
    --silver-light: #ffffff;
    --silver-mid: #b9bcc2;
    --silver-low: #e6e7ea;
    --firm-ink: #ffffff;
  }
  html, body {
    margin: 0;
    width: 1066px;
    height: 1200px;
    overflow: hidden;
    background: var(--page);
  }
  .canvas {
    position: relative;
    width: 1066px;
    height: 1200px;
  }
  .billboard {
    position: absolute;
    left: 0;
    top: 359px;
    width: 1066px;
    height: 481px;
    display: block;
  }
  .headline,
  .firm-name {
    font-family: "Bebas Neue", "Oswald", sans-serif;
  }
</style>
</head>
<body>
<main class="canvas">
  <svg class="billboard" viewBox="0 0 1066 481" xmlns="http://www.w3.org/2000/svg" aria-labelledby="bbTitle">
    <title id="bbTitle">Injured? Call Bruno! 318-555-0187 — Bruno Pemberly Accident &amp; Injury Lawyers</title>
    <defs>
      <linearGradient id="skyToGold" x1="0" y1="0" x2="0" y2="1">
        <stop offset="0" stop-color="var(--blue)"/>
        <stop offset="0.35" stop-color="var(--navy)"/>
        <stop offset="0.58" stop-color="#2a3560"/>
        <stop offset="0.72" stop-color="#8c7a3e"/>
        <stop offset="0.82" stop-color="var(--gold)"/>
        <stop offset="1" stop-color="var(--gold)"/>
      </linearGradient>
      <radialGradient id="portraitGlow" cx="0.5" cy="0.4" r="0.6">
        <stop offset="0" stop-color="var(--gold-soft)"/>
        <stop offset="0.5" stop-color="#b88a3a" stop-opacity="0.8"/>
        <stop offset="1" stop-color="var(--navy-deep)" stop-opacity="0"/>
      </radialGradient>
      <linearGradient id="portraitSuit" x1="0" y1="0" x2="0" y2="1">
        <stop offset="0" stop-color="#c99a55" stop-opacity="0.9"/>
        <stop offset="0.45" stop-color="#1d2a5c"/>
        <stop offset="1" stop-color="#1d2a5c" stop-opacity="0"/>
      </linearGradient>
      <linearGradient id="chrome" x1="0" y1="0" x2="0" y2="1">
        <stop offset="0" stop-color="var(--silver-light)"/>
        <stop offset="0.48" stop-color="var(--silver-light)"/>
        <stop offset="0.52" stop-color="var(--silver-mid)"/>
        <stop offset="1" stop-color="var(--silver-low)"/>
      </linearGradient>
      <linearGradient id="reflectFade" x1="0" y1="0" x2="0" y2="1">
        <stop offset="0" stop-color="#fff" stop-opacity="0"/>
        <stop offset="0.6" stop-color="#fff" stop-opacity="0"/>
        <stop offset="1" stop-color="#fff" stop-opacity="0.3"/>
      </linearGradient>
    </defs>

    <rect class="backdrop" width="1066" height="481" fill="url(#skyToGold)" role="img" aria-label="Dusk city skyline photograph fading from blue sky into gold"/>

    <g class="portrait" role="img" aria-label="Photo of the lawyer in a navy suit and green tie, raising a fist">
      <ellipse cx="543" cy="130" rx="150" ry="140" fill="url(#portraitGlow)"/>
      <path d="M420 343 L420 190 Q470 150 543 150 Q616 150 666 190 L666 343 Z" fill="url(#portraitSuit)"/>
    </g>

    <g class="headline">
      <text x="23" y="264" font-size="262" textLength="388" lengthAdjust="spacingAndGlyphs" fill="url(#chrome)">INJURED?</text>
      <text x="23" y="264" font-size="262" textLength="388" lengthAdjust="spacingAndGlyphs" fill="url(#reflectFade)" transform="translate(0 528) scale(1 -1)">INJURED?</text>

      <text x="669" y="200" font-size="172" textLength="358" lengthAdjust="spacingAndGlyphs" fill="url(#chrome)">CALL BRUNO!</text>
      <text x="678" y="270" font-size="87" textLength="349" lengthAdjust="spacingAndGlyphs" fill="url(#chrome)">318-555-0187</text>
      <text x="678" y="270" font-size="87" textLength="349" lengthAdjust="spacingAndGlyphs" fill="url(#reflectFade)" transform="translate(0 540) scale(1 -1)">318-555-0187</text>
    </g>

    <g class="firm-name" fill="var(--firm-ink)" text-anchor="middle">
      <text x="536" y="400" font-size="62" letter-spacing="2">BRUNO PEMBERLY</text>
      <text x="536" y="450" font-size="40" letter-spacing="2">ACCIDENT &amp; INJURY LAWYERS</text>
    </g>
  </svg>
</main>
</body>
</html>
```